Quenti Peruvian Cuisine needs a take-out menu

We need a new tri-fold 8.5"x11" take out menu for a Peruvian restaurant based in New Rochelle, NY. We have a vast selections of dishes from appetizers, seafood based dishes, desserts, Peruvian ceviches and more. We have attached the following:

Restaurant information
Pictures of our dishes
Quenti Logo in pdf format
Menu in word format
Old take out menu for reference only! (our dishes have changed)
Updates

Industry/Entity Type

Restaurant

```html
<!DOCTYPE html>
<html lang="en">
<head>
<meta charset="utf-8">
<title>Quenti Peruvian Cuisine – Take-out Menu</title>
<link rel="stylesheet" href="https://fonts.googleapis.com/css2?family=Great+Vibes&family=Roboto+Slab:wght@700&family=Lora:ital@1&display=swap">
<style>
  :root {
    --bg: #8f8f8f;
    --paper: #eadcc0;
    --paper-dark: #d9c6a2;
    --paper-light: #f3ead7;
    --ink: #1f2a4a;
    --accent: #9a2a1e;
    --price: #5a3a22;
    --band-brown: #5b2a14;
    --band-red: #8e1f17;
    --gold: #f2c94c;
  }
  * { box-sizing: border-box; margin: 0; padding: 0; }
  html, body { width: 900px; height: 1200px; overflow: hidden; background: var(--bg); }
  body { position: relative; }
  .spread {
    position: absolute; left: 75px; width: 750px; height: 580px;
    display: grid; grid-template-columns: repeat(3, 1fr);
    background: linear-gradient(135deg, var(--paper-light), var(--paper) 45%, var(--paper-dark));
    box-shadow: 0 6px 18px rgba(0,0,0,.35);
  }
  .spread.outside { top: 14px; }
  .spread.inside { top: 606px; }
  .panel { position: relative; padding: 12px 14px; overflow: hidden; border-right: 1px solid rgba(90,58,34,.18); }
  .panel:last-child { border-right: none; }
  .section-title {
    font-family: "Great Vibes", cursive; color: var(--ink); font-size: 26px;
    text-align: center; line-height: 1; margin: 4px 0 6px;
  }
  .section-title::before, .section-title::after { content: "~"; color: var(--accent); font-size: 16px; margin: 0 6px; vertical-align: middle; }
  .item { margin-bottom: 5px; }
  .item .row { display: flex; justify-content: space-between; align-items: baseline; }
  .item .name { font-family: "Roboto Slab", serif; font-weight: 700; font-size: 9px; color: var(--ink); text-transform: uppercase; }
  .item .price { font-family: "Lora", serif; font-style: italic; font-size: 9px; color: var(--price); white-space: nowrap; margin-left: 6px; }
  .item .desc { font-family: "Lora", serif; font-style: italic; font-size: 7.4px; line-height: 1.2; color: var(--accent); }
  .photo { border-radius: 4px; }
  .photo-top { height: 92px; margin: -12px -14px 8px; background: linear-gradient(120deg, #f4f1ea, #c9b79a 50%, #e7d2a8); }
  .photo-bottom { position: absolute; left: 0; right: 0; bottom: 0; height: 72px; background: linear-gradient(90deg, #f6f3ee, #9a4a26 45%, #d9822b 70%, #f6f3ee); }
  .photo-desserts { height: 80px; margin-top: 10px; background: linear-gradient(120deg, #f4f1ea, #c8893a 50%, #e2b068); }
  .photo-inline { height: 48px; margin: 6px 0; background: linear-gradient(90deg, #f4f1ea, #8c4a2a 50%, #c9a36b); }
  .cover { display: flex; flex-direction: column; align-items: center; padding: 14px 0 0; background: linear-gradient(180deg, #f0e3c8, #e8c79a); }
  .brand { display: flex; align-items: center; gap: 6px; font-family: "Roboto Slab", serif; font-weight: 700; font-size: 15px; color: var(--ink); }
  .brand .dot { width: 12px; height: 12px; border-radius: 50%; background: #7aa55a; }
  .tagline { font-family: "Lora", serif; font-style: italic; font-size: 9px; color: var(--accent); margin-top: 2px; }
  .cover-art { width: 220px; height: 250px; margin-top: 10px; border-radius: 6px; background: radial-gradient(circle at 50% 35%, #8a4a22, #c8893a 45%, #e9cf9a 75%); }
  .contact { width: 100%; margin-top: 14px; }
  .band { color: #fff; text-align: center; font-family: "Roboto Slab", serif; font-weight: 700; }
  .band.address { background: var(--band-brown); font-size: 9px; padding: 4px 0 2px; color: var(--gold); }
  .band.phone { background: var(--band-brown); font-size: 20px; padding: 0 0 6px; display: flex; justify-content: center; align-items: center; gap: 8px; }
  .band.hours { background: #6e3418; font-size: 9px; padding: 5px 0; color: var(--gold); line-height: 1.4; }
  .band.note { background: var(--band-red); font-family: "Lora", serif; font-style: italic; font-weight: 400; font-size: 8px; padding: 6px 10px; line-height: 1.35; }
  .photo-caption { position: absolute; right: 10px; bottom: 4px; font-family: "Lora", serif; font-style: italic; font-size: 8px; color: #333; }
</style>
</head>
<body>

<!-- Outside of the tri-fold -->
<section class="spread outside">
  <div class="panel">
    <div class="photo photo-top" role="img" aria-label="Photos of ceviche and a creamy seafood dish"></div>
    <div class="item"><div class="row"><span class="name">Aeropuerto</span><span class="price">$ 18.95</span></div><div class="desc">peruvian style fried rice, mixed with noodles, chicken, beef and shrimp –</div></div>
    <div class="item"><div class="row"><span class="name">Arroz Chaufa</span><span class="price">$ 14.95</span></div><div class="desc">peruvian style fried rice mixed with choice of beef or chicken Carne – Pollo – 12.95</div></div>
    <div class="item"><div class="row"><span class="name">Seco de Carne</span><span class="price">$ 15.95</span></div><div class="desc">beef ribs stew in aji panka sauce, served with rice and Peruvian canario beans –</div></div>
    <div class="item"><div class="row"><span class="name">Aji de Gallina</span><span class="price">$ 11.95</span></div><div class="desc">shredded chicken in a spicy aji amarillo creamy sauce, hard-boiled egg, olives, potatoes and rice –</div></div>
    <h2 class="section-title">Seafood</h2>
    <div class="item"><div class="row"><span class="name">Pescado a lo Macho</span><span class="price">$ 19.95</span></div><div class="desc">fried fish fillet topped with seafood in hot yellow pepper sauce, served with rice and yuccas –</div></div>
    <div class="item"><div class="row"><span class="name">Pescado Sudado</span><span class="price">$ 16.95</span></div><div class="desc">corvina fish stew in hot yellow pepper, tomatoes, onions, served with yuccas and rice –</div></div>
    <div class="item"><div class="row"><span class="name">Arroz con Mariscos</span><span class="price">$ 17.95</span></div><div class="desc">peruvian style paella, red rice served with seafood –</div></div>
    <div class="item"><div class="row"><span class="name">Arroz Chaufa</span><span class="price">$ 17.95</span></div><div class="desc">peruvian style fried rice served with choice of seafood or shrimp Mariscos – Camarones – 17.95</div></div>
    <div class="item"><div class="row"><span class="name">Trucha Frita</span><span class="price">$ 18.95</span></div><div class="desc">deep fried Trout, served with white rice, fried yuccas and salsa criolla –</div></div>
    <div class="item"><div class="row"><span class="name">Jalea</span><span class="price">$ 28.95</span></div><div class="desc">deep fried mixed seafood and fish, served with fried yuccas Large – Small – 17.95</div></div>
  </div>

  <div class="panel">
    <h2 class="section-title">Chicken</h2>
    <div class="item"><div class="row"><span class="name">1/4 Pollo</span><span class="price">$ 6.50</span></div><div class="desc">quarter chicken, served with two sides –</div></div>
    <div class="item"><div class="row"><span class="name">1/2 Pollo</span><span class="price">$ 8.95</span></div><div class="desc">half chicken, served with two sides –</div></div>
    <div class="item"><div class="row"><span class="name">1 Pollo</span><span class="price">$ 16.95</span></div><div class="desc">whole chicken, served with two sides –</div></div>
    <div class="item"><div class="row"><span class="name">Pollo Limeño</span><span class="price">$ 20.95</span></div><div class="desc">whole chicken, served with French fries, avocado salad and yellow rice –</div></div>
    <div class="item"><div class="row"><span class="name">Pollo Chalaco</span><span class="price">$ 26.95</span></div><div class="desc">whole chicken, served with avocado salad, salchipapa and yellow rice –</div></div>
    <div class="item"><div class="row"><span class="name">Pollo Quenti</span><span class="price">$ 30.95</span></div><div class="desc">whole chicken, served with avocado salad, arroz chaufa (chicken or steak) and salchipapa –</div></div>
    <h2 class="section-title">Desserts</h2>
    <div class="item"><div class="row"><span class="name">Crema Volteada</span><span class="price">$ 5.95</span></div><div class="desc">Peruvian caramel custard –</div></div>
    <div class="item"><div class="row"><span class="name">Tres Lech</span><span class="price">$ 5.95</span></div><div class="desc">Butter cake soaked in three kinds of milk –</div></div>
    <div class="item"><div class="row"><span class="name">Torta Helada</span><span class="price">$ 5.95</span></div><div class="desc">Sponge cake topped with strawberry jello –</div></div>
    <div class="item"><div class="row"><span class="name">Torta de Chocholate</span><span class="price">$ 5.95</span></div><div class="desc">Chocolate cake –</div></div>
    <div class="item"><div class="row"><span class="name">Picarones</span><span class="price">$ 5.95</span></div><div class="desc">Peruvian style sweet potato doughnut covered with syrup –</div></div>
    <div class="photo photo-desserts" role="img" aria-label="Photos of picarones and empanada with dipping sauce"></div>
  </div>

  <div class="panel cover">
    <div class="brand"><span class="dot"></span>Quenti</div>
    <div class="tagline">Peruvian Cuisine</div>
    <div class="cover-art" role="img" aria-label="Roasted rotisserie chicken on a plate with a cartoon chef illustration"></div>
    <div class="contact">
      <div class="band address">212 Elm Row, Pinecrest, NY 10999</div>
      <div class="band phone">
        <svg width="16" height="16" viewBox="0 0 24 24" aria-hidden="true"><path fill="#f2c94c" d="M6.6 10.8a15 15 0 0 0 6.6 6.6l2.2-2.2c.3-.3.7-.4 1-.2 1.1.4 2.3.6 3.6.6.6 0 1 .4 1 1V20c0 .6-.4 1-1 1A17 17 0 0 1 3 4c0-.6.4-1 1-1h3.5c.6 0 1 .4 1 1 0 1.3.2 2.5.6 3.6.1.3 0 .7-.2 1z"/></svg>
        555-013-4829
      </div>
      <div class="band hours">Delivery Hours<br>Mon - Sun &nbsp;|&nbsp; 11:30 am – 10 pm</div>
      <div class="band note">Notes: Deliveries on order of $15 or more. $5 fee for 3 miles or more. Chef's specials on weekends.</div>
    </div>
  </div>
</section>

<!-- Inside of the tri-fold -->
<section class="spread inside">
  <div class="panel">
    <h2 class="section-title">Appetizers</h2>
    <div class="item"><div class="row"><span class="name">Chicharron de Calamares</span><span class="price">$ 12.95</span></div><div class="desc">crispy fried calamari served with house tartar sauce and salsa criolla –</div></div>
    <div class="item"><div class="row"><span class="name">Anticucho Carretiller</span><span class="price">$ 15.95</span></div><div class="desc">choice chicken or cow's heart Peruvian style kebabs, served with Cusco corn and grilled potatoes Corazon – Pollo –</div></div>
    <div class="item"><div class="row"><span class="name">Palta Rellena</span><span class="price">$ 15.95</span></div><div class="desc">peruvian avocado stuffed with choice of chicken or shrimp, marinated in Peruvian spices Camarones – Pollo – 11.95</div></div>
    <div class="item"><div class="row"><span class="name">Tamal Criollo</span><span class="price">$ 8.95</span></div><div class="desc">peruvian chicken tamale, served with salsa criolla –</div></div>
    <div class="item"><div class="row"><span class="name">Salchipapa</span><span class="price">$ 5.95</span></div><div class="desc">french fries mixed with sliced hot dogs –</div></div>
    <div class="item"><div class="row"><span class="name">Papa a la Huancaina</span><span class="price">$ 9.95</span></div><div class="desc">boiled potatoes, topped with aji amarillo and queso fresco sauce, egg, olives –</div></div>
    <div class="item"><div class="row"><span class="name">Ocopa Arequipeña</span><span class="price">$ 8.95</span></div><div class="desc">boiled potatoes, topped with huacatay sauce and queso fresco, egg, olives –</div></div>
    <div class="item"><div class="row"><span class="name">Empanada Limeña</span><span class="price">$ 3.95</span></div><div class="desc">patties stuffed with choice of chicken or beef –</div></div>
    <div class="item"><div class="row"><span class="name">Causa</span><span class="price">$ 9.95</span></div><div class="desc">cold mashed potato infused with key lime juice, pressed into a cake with chicken or shrimp Camarones – Pollo – 7.95</div></div>
    <div class="item"><div class="row"><span class="name">Choritos a la Chalaca</span><span class="price">$ 10.95</span></div><div class="desc">steamed mussels topped with diced onions, tomatoes, lime juice and Cusco corn –</div></div>
    <div class="item"><div class="row"><span class="name">Piqueo Quenti</span><span class="price">$ 19.95</span></div><div class="desc">Combined Chicharron de Calamares, Papa a la Huancaina, Choritos and Causa</div></div>
    <div class="photo photo-bottom" role="img" aria-label="Photo of lomo saltado with fries and tomatoes"></div>
    <span class="photo-caption">Lomo Saltado</span>
  </div>

  <div class="panel">
    <h2 class="section-title">Salads</h2>
    <div class="item"><div class="row"><span class="name">Ensalada de la Casa</span><span class="price">$ 6.95</span></div><div class="desc">lettuce, tomatoes, yellow peppers and zucchini –</div></div>
    <div class="item"><div class="row"><span class="name">Ensalada Quenti</span><span class="price">$ 7.95</span></div><div class="desc">lettuce, tomatoes, cucumbers, red onions, carrots, radish and avocado –</div></div>
    <div class="item"><div class="row"><span class="name">Ensalada Cesar</span><span class="price">$ 8.95</span></div><div class="desc">romaine, lettuce, croutons, parmesan cheese and Quenti's special sauce –</div></div>
    <h2 class="section-title">Soups</h2>
    <div class="item"><div class="row"><span class="name">Aguadito Limeño</span><span class="price">$ 9.95</span></div><div class="desc">chicken and vegetable soup mixed with rice and cilantro Large – Small – 5.95</div></div>
    <div class="item"><div class="row"><span class="name">Sopa a la Minuta</span><span class="price">$ 12.95</span></div><div class="desc">traditional milk and angel's hair pasta soup, served with beef and eggs –</div></div>
    <div class="item"><div class="row"><span class="name">Caldo de Gallina</span><span class="price">$ 12.95</span></div><div class="desc">hen broth with noodles, scallion, potatoes and hard-boiled egg –</div></div>
    <div class="item"><div class="row"><span class="name">Chupe de Camarones Arequipeño</span><span class="price">$ 15.95</span></div><div class="desc">shrimp soup mixed with rice, green peas, Cusco corn, milk, eggs and Peruvian spices –</div></div>
    <div class="item"><div class="row"><span class="name">Parihuela del Puerto</span><span class="price">$ 18.95</span></div><div class="desc">classic Peruvian seafood soup –</div></div>
    <h2 class="section-title">Ceviches</h2>
    <div class="item"><div class="row"><span class="name">Leche de Tigre</span><span class="price">$ 10.95</span></div><div class="desc">ceviche marinade in fresh lime juice –</div></div>
    <div class="item"><div class="row"><span class="name">Tiradito en Salsa de Aji Amarillo</span><span class="price">$ 12.95</span></div><div class="desc">sashimi style fish in yellow pepper sauce and fresh lime juice, served with Cusco corn and sweet potatoes –</div></div>
    <div class="item"><div class="row"><span class="name">Piqueo Chalaco</span><span class="price">$ 24.95</span></div><div class="desc">dish combined of Ceviche de Pescado (Fish Ceviche) and Jalea (Fried Seafood) –</div></div>
    <div class="item"><div class="row"><span class="name">Ceviche</span><span class="price">$ 15.95</span></div><div class="desc">choice of raw fish, mixed seafood, shrimp or shrimp with octopus, marinated in fresh lime juice, red onions, Cusco corn and sweet potatoes Pescado – Camaron – 17.95 | Mixto – 17.95 | Camaron con Pulpo – 18.95</div></div>
  </div>

  <div class="panel">
    <h2 class="section-title">Sides</h2>
    <div class="item"><div class="row"><span class="name">Papas Fritas</span><span class="price">$ 3.95</span></div><div class="desc">french fries –</div></div>
    <div class="item"><div class="row"><span class="name">Arroz Blanco o Amarillo</span><span class="price">$ 3.95</span></div><div class="desc">white/yellow rice –</div></div>
    <div class="item"><div class="row"><span class="name">Frejoles</span><span class="price">$ 3.95</span></div><div class="desc">peruvian canario beans –</div></div>
    <div class="item"><div class="row"><span class="name">Maduros</span><span class="price">$ 3.95</span></div><div class="desc">sweet plantains –</div></div>
    <div class="item"><div class="row"><span class="name">Tostones</span><span class="price">$ 3.95</span></div><div class="desc">fried green plantains –</div></div>
    <div class="item"><div class="row"><span class="name">Yuca Frita</span><span class="price">$ 3.95</span></div><div class="desc">fried yuccas –</div></div>
    <div class="photo photo-inline" role="img" aria-label="Photos of pan-seared meat dishes"></div>
    <h2 class="section-title">Traditional Dishes</h2>
    <div class="item"><div class="row"><span class="name">Parrillada Mixta</span><span class="price">$ 30.95</span></div><div class="desc">dish combined of grilled NY Strip steak, anticuchos (Peruvian style kebabs), pork chops and sausage –</div></div>
    <div class="item"><div class="row"><span class="name">Churrasco en Salsa de Camarones</span><span class="price">$ 20.95</span></div><div class="desc">NY strip steak topped with shrimps on hot yellow pepper sauce, served with rice –</div></div>
    <div class="item"><div class="row"><span class="name">Seco Norteño</span><span class="price">$ 20.95</span></div><div class="desc">slowly cooked lamb stew in aji panka sauce, served with rice and Peruvian canario beans –</div></div>
    <div class="item"><div class="row"><span class="name">Seco de Pato Piurano</span><span class="price">$ 17.95</span></div><div class="desc">slowly cooked duck stew in aji panka sauce, served with rice and hard-boiled yuccas –</div></div>
    <div class="item"><div class="row"><span class="name">Tallarines Verdes con Churrasco</span><span class="price">$ 18.95</span></div><div class="desc">linguine pasta in Peruvian style pesto sauce served with grilled NY Strip steak –</div></div>
    <div class="item"><div class="row"><span class="name">Tacu Tacu</span><span class="price">$ 18.95</span></div><div class="desc">peruvian canario beans mixed with rice, served with choice of NY Strip steak or wok-seared beef in soy sauce Churrasco – Lomo – 15.95</div></div>
    <div class="item"><div class="row"><span class="name">Churrasco a lo Pobre</span><span class="price">$ 19.95</span></div><div class="desc">NY strip steak served with fried eggs, sweet plantains, French fries and rice –</div></div>
    <div class="item"><div class="row"><span class="name">Saltado</span><span class="price">$ 15.95</span></div><div class="desc">choice of wok-seared steak or chicken, mixed with red onions, tomatoes, in soy sauce, served with French fries and rice Lomo – Pollo – 13.95</div></div>
  </div>
</section>

</body>
</html>
```